Modern business card for triathlon training business in Australia

We need a business card design for our triathlon training company.

Lakeshore Pace Fitness is an Australian business, owned by women, run for women. Lakeshore Pace Fitness helps women prepare or improve triathlon skills and confidence through triathlon camps completely designed for women.

Our camps focus on preparing women both physically and mentally for their next (or first!) triathlon.

You can see our website www.lakeshorepacefitness.com.au for more info about our business and our style.

We've attached two of our logos and are happy to consider a design that utilised either colour scheme with the teal colour being our 'feature' colour. We don't want overly feminine cards but rather cards that are professional and neat. If the inclusion of any pictures/art is warranted, this should be focused on our swim/ride/run theme and in that specific order (swim/ride/run).

The business card needs to be a printable design and the contact details will need to change for our two employees.

Target Market(s)

Female clients and partners/vendors/sponsors that we work with in the triathlon industry

Industry/Entity Type

Fitness

Contact Information for Business Card

Lakeshore Pace Fitness (business name)
Maren Dunley
Business Director
Mobile: 0455 918 237
Email: maren@lakeshorepacefitness.com.au
www.lakeshorepacefitness.com.au

Second business card:
Lakeshore Pace Fitness
Bea Calvert
Coaching Director
Mobile: 0433 206 519
Email: bea@lakeshorepacefitness.com.au

Font styles to use
Serif
Sans Serif

Requirements
Must have
• Core contact details above, our logo and be a printable design
Should not have
• Pink
• Cursive/script fonts

```html
<!DOCTYPE html>
<html lang="en">
<head>
<meta charset="utf-8">
<title>Lakeshore Pace Fitness – Business Cards</title>
<link rel="stylesheet" href="https://fonts.googleapis.com/css2?family=Open+Sans:wght@400;600;700&display=swap">
<style>
  :root {
    --teal: #1fbfcf;
    --teal-deep: #179dad;
    --ink: #ffffff;
    --page: #ffffff;
  }
  * { margin: 0; padding: 0; box-sizing: border-box; }
  html, body { width: 1200px; height: 1000px; overflow: hidden; background: var(--page); }
  body { position: relative; font-family: "Open Sans", Arial, sans-serif; color: var(--ink); }

  .swatch { position: absolute; left: 0; width: 50px; height: 50px; }
  .swatch--light { top: 0; background: var(--teal); }
  .swatch--deep { top: 50px; background: var(--teal-deep); }

  .card { position: absolute; background: var(--teal); overflow: hidden; white-space: nowrap; }
  .card--landscape { width: 400px; height: 258px; }
  .card--portrait { width: 259px; height: 399px; }

  .card__band { position: absolute; left: 0; right: 0; height: 63px; background: var(--teal-deep); }
  .card--landscape .card__band { top: 98px; }
  .card--portrait .card__band { top: 179px; }

  .brand { position: absolute; font-weight: 700; color: var(--ink); line-height: 1.05; }
  .brand__mark { display: inline-block; width: 10px; height: 10px; background: var(--ink); margin-right: 7px; vertical-align: 1px; }

  .person { position: absolute; }
  .person__name { font-size: 20px; font-weight: 600; line-height: 24px; }
  .person__role { font-size: 14px; line-height: 18px; }

  .contact { position: absolute; font-size: 14.5px; line-height: 18.5px; }
  .web { position: absolute; font-size: 14.5px; }

  /* centred landscape */
  .card--centred .brand { top: 34px; left: 0; right: 0; text-align: center; font-size: 19px; }
  .card--centred .person,
  .card--centred .contact,
  .card--centred .web { left: 0; right: 0; text-align: center; }
  .card--centred .person { top: 108px; }
  .card--centred .contact { top: 171px; }
  .card--centred .web { top: 225px; }

  /* left-aligned landscape */
  .card--aligned .brand { top: 28px; left: 15px; font-size: 17px; width: 160px; white-space: normal; }
  .card--aligned .person,
  .card--aligned .contact,
  .card--aligned .web { left: 100px; }
  .card--aligned .person { top: 108px; }
  .card--aligned .contact { top: 171px; font-size: 13.5px; }
  .card--aligned .web { top: 225px; font-size: 13.5px; }

  /* portrait */
  .card--portrait .brand { top: 60px; left: 0; right: 0; text-align: center; font-size: 30px; white-space: normal; }
  .card--portrait .person,
  .card--portrait .contact,
  .card--portrait .web { left: 0; right: 0; text-align: center; }
  .card--portrait .person { top: 189px; }
  .card--portrait .contact { top: 257px; font-size: 11px; line-height: 18px; }
  .card--portrait .web { top: 366px; font-size: 13px; }
</style>
</head>
<body>
  <div class="swatch swatch--light"></div>
  <div class="swatch swatch--deep"></div>

  <!-- Row 1: centred -->
  <section class="card card--landscape card--centred" style="left:200px;top:20px;">
    <div class="card__band"></div>
    <div class="brand">Lakeshore Pace Fitness</div>
    <div class="person"><div class="person__name">Maren Dunley</div><div class="person__role">Business Director</div></div>
    <div class="contact">Mobile: 0455 918 237<br>Email: maren@lakeshorepacefitness.com.au</div>
    <div class="web">www.lakeshorepacefitness.com.au</div>
  </section>
  <section class="card card--landscape card--centred" style="left:650px;top:20px;">
    <div class="card__band"></div>
    <div class="brand">Lakeshore Pace Fitness</div>
    <div class="person"><div class="person__name">Bea Calvert</div><div class="person__role">Coaching Director</div></div>
    <div class="contact">Mobile: 0433 206 519<br>Email: bea@lakeshorepacefitness.com.au</div>
    <div class="web">www.lakeshorepacefitness.com.au</div>
  </section>

  <!-- Row 2: aligned -->
  <section class="card card--landscape card--aligned" style="left:200px;top:300px;">
    <div class="card__band"></div>
    <div class="brand">Lakeshore Pace Fitness</div>
    <div class="person"><div class="person__name">Maren Dunley</div><div class="person__role">Business Director</div></div>
    <div class="contact">Mobile: 0455 918 237<br>Email: bea@lakeshorepacefitness.com.au</div>
    <div class="web">www.lakeshorepacefitness.com.au</div>
  </section>
  <section class="card card--landscape card--aligned" style="left:650px;top:300px;">
    <div class="card__band"></div>
    <div class="brand">Lakeshore Pace Fitness</div>
    <div class="person"><div class="person__name">Bea Calvert</div><div class="person__role">Coaching Director</div></div>
    <div class="contact">Mobile: 0433 206 519<br>Email: bea@lakeshorepacefitness.com.au</div>
    <div class="web">www.lakeshorepacefitness.com.au</div>
  </section>

  <!-- Row 3: portrait -->
  <section class="card card--portrait" style="left:270px;top:580px;">
    <div class="card__band"></div>
    <div class="brand">Lakeshore Pace<br>Fitness</div>
    <div class="person"><div class="person__name">Maren Dunley</div><div class="person__role">Business Director</div></div>
    <div class="contact">Mobile: 0455 918 237<br>Email: maren@lakeshorepacefitness.com.au</div>
    <div class="web">www.lakeshorepacefitness.com.au</div>
  </section>
  <section class="card card--portrait" style="left:720px;top:580px;">
    <div class="card__band"></div>
    <div class="brand">Lakeshore Pace<br>Fitness</div>
    <div class="person"><div class="person__name">Bea Calvert</div><div class="person__role">Coaching Director</div></div>
    <div class="contact">Mobile: 0433 206 519<br>Email: bea@lakeshorepacefitness.com.au</div>
    <div class="web">www.lakeshorepacefitness.com.au</div>
  </section>
</body>
</html>
```